Deisgn A Manual Cover for an Australian Health Training Company

We are looking for an A4 Front of Manual Cover Design for a comprehensive administrative training manual to be launched soon in Australia.

The title of the book is :

"Drafting, Shaping and Delivering Office Paperwork"

for the Australian Medical Office (smaller font)

Written and compiled by Mel Trosk

Target Market(s)

25-45 year old medical administrative students (usually female)

Industry/Entity Type

It Company

Font styles to use
Serif

Colors
3176b5
f68d4c
33b8a4
fffbf0

Requirements
Must have
• University like perhaps
• Human element (picture/s of people)
• About the concept of designing and producing documents in a health setting (this can be entirely conceptual).
• Conceptual design would be considered
• Appealing

```html
<!DOCTYPE html>
<html lang="en">
<head>
<meta charset="utf-8">
<title>Drafting, Shaping and Delivering Office Paperwork — Manual Cover</title>
<link rel="stylesheet" href="https://fonts.googleapis.com/css2?family=Archivo+Black&family=Open+Sans:ital,wght@0,400;1,300&display=swap">
<style>
  :root {
    --blue: #3176b5;
    --orange: #f68d4c;
    --teal: #33b8a4;
    --ink: #111111;
    --paper: #ffffff;
  }
  html, body {
    margin: 0;
    padding: 0;
    overflow: hidden;
    background: var(--paper);
  }
  .cover {
    position: relative;
    width: 849px;
    height: 1200px;
    overflow: hidden;
    background: var(--paper);
    color: var(--ink);
  }
  .byline {
    position: absolute;
    left: 40px;
    top: 34px;
    margin: 0;
    font-family: "Open Sans", sans-serif;
    font-style: italic;
    font-weight: 300;
    font-size: 27px;
    line-height: 36px;
  }
  .colour-field {
    position: absolute;
    left: 470px;
    top: 0;
    width: 379px;
    height: 1200px;
    background:
      linear-gradient(180deg,
        rgba(49, 118, 181, .55) 0%,
        rgba(246, 141, 76, .45) 22%,
        rgba(51, 184, 164, .5) 45%,
        rgba(49, 118, 181, .55) 68%,
        rgba(246, 141, 76, .5) 100%);
  }
  .title {
    position: absolute;
    left: 38px;
    top: 650px;
    margin: 0;
    font-family: "Archivo Black", sans-serif;
    font-weight: 400;
    font-size: 70px;
    line-height: 69px;
    letter-spacing: -2px;
  }
  .title .line { display: block; }
  .title .joiner {
    font-size: 30px;
    letter-spacing: -0.5px;
  }
  .subtitle {
    position: absolute;
    left: 40px;
    top: 1118px;
    margin: 0;
    font-family: "Open Sans", sans-serif;
    font-weight: 400;
    font-size: 22px;
    line-height: 26px;
  }
</style>
</head>
<body>
<main class="cover">
  <div class="colour-field" role="img" aria-label="Decorative pattern of overlapping translucent vertical bars in blue, orange and teal"></div>

  <p class="byline">Written and compiled<br>by Mel Trosk</p>

  <h1 class="title">
    <span class="line">Drafting,</span>
    <span class="line">Shaping <span class="joiner">and</span></span>
    <span class="line">Delivering</span>
    <span class="line">Office</span>
    <span class="line">Paperwork</span>
  </h1>

  <p class="subtitle">for the Australian<br>Medical Office</p>
</main>
</body>
</html>
```